iron deficiency anemia - educational reference paper

looking for an educational paper/poster 8x11 or no larger than 11x14 that lists the most common foods with pictures and limited words a super rough outline attached - I wrote the words of the pictures (but would like to have the actual pictures of these items) I would like in roughly the same order
for the pictures for fatigue, headache....can be drawings or cartoons
double sided or single sided (which ever fits) see attached for categories (3 of them)

Target Market(s)

educational for people with limited education - thus not much wording

Requirements
Must have
• pictures, simple design

```html
<!DOCTYPE html>
<html lang="en">
<head>
<meta charset="utf-8">
<title>Iron Deficiency Anemia</title>
<link rel="stylesheet" href="https://fonts.googleapis.com/css2?family=Archivo+Black&family=Open+Sans:wght@400;600;700&display=swap">
<style>
  :root {
    --page-bg: #e9e7e4;
    --paper: #ffffff;
    --red: #c3191f;
    --red-dark: #8e0f14;
    --ink: #111111;
    --charcoal: #3b3b3d;
    --grey-text: #555555;
    --soft-grey: #eeeeee;
  }
  html, body {
    margin: 0;
    padding: 0;
    width: 1200px;
    height: 818px;
    overflow: hidden;
    background: var(--page-bg);
    font-family: "Open Sans", Arial, sans-serif;
  }
  .flyer {
    position: absolute;
    left: 293px;
    top: 13px;
    width: 613px;
    height: 792px;
    background: var(--paper);
    overflow: hidden;
    box-shadow: 0 2px 8px rgba(0,0,0,.15);
  }
  .flyer-bg { position: absolute; inset: 0; }
  .title {
    position: absolute;
    left: 36px;
    top: 28px;
    margin: 0;
    font-family: "Archivo Black", Arial, sans-serif;
    font-size: 34px;
    line-height: 36px;
    letter-spacing: 0.5px;
    color: var(--ink);
  }
  .title .accent { color: var(--red); display: block; }
  .foods-heading {
    position: absolute;
    left: 44px;
    top: 314px;
    margin: 0;
    font-size: 11.5px;
    font-weight: 700;
    letter-spacing: 0.4px;
    color: #fff;
  }
  .food-list {
    position: absolute;
    top: 339px;
    margin: 0;
    padding: 0;
    list-style: none;
    font-size: 9px;
    line-height: 11.4px;
    color: #fff;
  }
  .food-list li::before { content: "•"; margin-right: 6px; font-size: 7px; }
  .symptoms-pill {
    position: absolute;
    left: 208px;
    top: 510px;
    width: 194px;
    height: 25px;
    border-radius: 13px;
    background: var(--charcoal);
    color: #fff;
    font-size: 11px;
    font-weight: 700;
    letter-spacing: 0.5px;
    text-align: center;
    line-height: 25px;
  }
  .symptom {
    position: absolute;
    top: 546px;
    width: 110px;
    text-align: center;
    font-size: 11px;
    color: var(--grey-text);
  }
  .symptom-icon {
    display: block;
    width: 62px;
    height: 62px;
    margin: 0 auto 8px;
    border-radius: 50%;
    background: radial-gradient(circle at 50% 45%, #d63a3f, var(--red));
    box-shadow: 0 0 0 2px #fff, 0 0 0 3px #c9c9c9;
  }
  .signs-rule {
    position: absolute;
    left: 18px;
    right: 18px;
    top: 650px;
    height: 1px;
    background: #999;
  }
  .signs-heading {
    position: absolute;
    left: 0;
    right: 0;
    top: 642px;
    text-align: center;
  }
  .signs-heading span {
    background: var(--paper);
    padding: 0 12px;
    font-size: 11px;
    font-weight: 700;
    letter-spacing: 0.5px;
    color: var(--charcoal);
  }
  .signs-heading span::before, .signs-heading span::after {
    content: "";
    display: inline-block;
    width: 5px; height: 5px;
    border-radius: 50%;
    background: var(--red);
    vertical-align: middle;
    margin: 0 10px;
  }
  .sign-photo {
    position: absolute;
    top: 669px;
    width: 127px;
    height: 88px;
    border-radius: 4px;
  }
  .bottom-bar {
    position: absolute;
    left: 0; right: 0; bottom: 0;
    height: 9px;
    background: var(--charcoal);
  }
</style>
</head>
<body>
<main class="flyer">
  <svg class="flyer-bg" width="613" height="792" viewBox="0 0 613 792">
    <defs>
      <linearGradient id="redWash" x1="0" y1="0" x2="1" y2="1">
        <stop offset="0" stop-color="#d42228"/>
        <stop offset="1" stop-color="#a9141a"/>
      </linearGradient>
      <linearGradient id="foodTones" x1="0" y1="0" x2="1" y2="1">
        <stop offset="0" stop-color="#d8d4cf"/>
        <stop offset="0.4" stop-color="#c79a6a"/>
        <stop offset="0.7" stop-color="#c96a4c"/>
        <stop offset="1" stop-color="#7a8f4a"/>
      </linearGradient>
    </defs>
    <rect x="0" y="0" width="613" height="560" fill="url(#redWash)"/>
    <rect x="0" y="0" width="613" height="8" fill="#6a6a6c"/>
    <path d="M0 8 H613 V290 C500 320 380 330 300 300 C180 255 70 210 0 150 Z" fill="#f2f2f4"/>
    <path d="M285 8 H613 V290 C500 320 380 330 300 300 C275 210 262 110 285 8 Z" fill="url(#foodTones)" role="img" aria-label="Photo of iron-rich foods: meat, salmon, eggs, cheese, nuts, beans, broccoli and artichokes"/>
    <path d="M0 528 C200 468 430 468 613 560" fill="none" stroke="#555" stroke-width="12"/>
    <path d="M0 536 C200 478 430 478 613 566 V792 H0 Z" fill="var(--paper)"/>
    <path d="M0 540 C200 484 430 484 613 570 V640 H0 Z" fill="var(--soft-grey)" opacity="0.6"/>
  </svg>

  <h1 class="title">IRON<br>DEFICIENCY<span class="accent">ANEMIA</span></h1>

  <h2 class="foods-heading">COMMON FOODS IN YOUR COMMUNITY</h2>
  <ul class="food-list" style="left:46px">
    <li>Sheep/lamb</li><li>Goose</li><li>Whale</li><li>Winged Bean</li><li>Rice Bran</li><li>White Bean</li><li>Pig/pork</li><li>Kidney Bean</li><li>Cowpea</li><li>Black Bean</li><li>Mung Bean</li>
  </ul>
  <ul class="food-list" style="left:152px">
    <li>Natto</li><li>Teff</li><li>Amaranth</li><li>Yardlong Bean</li><li>Chili/pink Bean</li><li>Lentil</li><li>Yellow Bean</li><li>Duck</li><li>Lima Bean</li><li>Chicken</li><li>Clams</li>
  </ul>
  <ul class="food-list" style="left:270px">
    <li>Pumpkin Seed</li><li>Squab</li><li>Pigeon Pea</li><li>Fava Bean</li><li>Sesame Seed</li><li>Aduzki Bean</li><li>Cranberry Bean</li><li>Masa</li><li>Split Peas</li><li>Cuttlefish</li><li>Bear</li>
  </ul>
  <ul class="food-list" style="left:393px">
    <li>Sunflower Seed</li><li>Bagel</li><li>Sardines</li><li>Chickpeas</li><li>Shrimp</li><li>Spinach</li><li>Beet</li><li>Brussle</li><li>Sprouts</li><li>Egg</li><li>Collard Greens</li>
  </ul>
  <ul class="food-list" style="left:520px">
    <li>Muschrooms</li><li>Nuts</li><li>Potatoe</li><li>Tortilla</li><li>Turkey</li><li>Blackberry</li><li>Broccoli</li><li>Carrot</li><li>Califlower</li><li>Halibut</li><li>Tomatoe</li>
  </ul>

  <div class="symptoms-pill">SYMPTOMS OF ANEMIA</div>
  <div class="symptom" style="left:48px"><span class="symptom-icon" role="img" aria-label="Drawing of a tired person"></span>Fatigue</div>
  <div class="symptom" style="left:145px"><span class="symptom-icon" role="img" aria-label="Drawing of a person holding their head in pain"></span>Headache</div>
  <div class="symptom" style="left:247px"><span class="symptom-icon" role="img" aria-label="Drawing of a dizzy person"></span>Dizziness</div>
  <div class="symptom" style="left:350px"><span class="symptom-icon" role="img" aria-label="Drawing of a person with blurry vision"></span>Blurry Vision</div>
  <div class="symptom" style="left:451px"><span class="symptom-icon" role="img" aria-label="Drawing of a weak, bent-over person"></span>Muscle Weakness</div>

  <div class="signs-rule"></div>
  <div class="signs-heading"><span>SIGNS OF ANEMIA</span></div>
  <div class="sign-photo" style="left:38px;background:linear-gradient(135deg,#6a8a90,#c99d84,#e0b9a0)" role="img" aria-label="Photo of pale palms"></div>
  <div class="sign-photo" style="left:171px;background:linear-gradient(135deg,#f0eeee,#c9a3a8,#9a6a78)" role="img" aria-label="Photo of spoon-shaped fingernails"></div>
  <div class="sign-photo" style="left:313px;background:linear-gradient(135deg,#d9b9a3,#f2ebe6,#c79a82)" role="img" aria-label="Photo of a pale lower eyelid"></div>
  <div class="sign-photo" style="left:445px;background:linear-gradient(135deg,#8a5a4e,#e3a2a0,#7a4c40)" role="img" aria-label="Photo of a pale, smooth tongue"></div>

  <div class="bottom-bar"></div>
</main>
</body>
</html>
```